Information Security Company Business Cards

Using our included logo, we need a business card design. It should have standard contact information such as :

Ravi Tanner
Senior Security Engineer
ravi.tanner@quorvex-hub.com
877.640.3958

Maybe include the website "www.quorvex-hub.com" that we will be redesigning soon.??

open to suggestions of course...

Target Market(s)

Our customers are small to large companies. Generally health-care, financial, insurance and the like.

Industry/Entity Type

Business

Font styles to use
Other font styles liked:
• Something that works with the logo

Requirements
Must have
• Colors should flow with the logo if possible. Or at least we think it should.

```html
<!DOCTYPE html>
<html lang="en">
<head>
<meta charset="utf-8">
<title>Quorvex Hub Business Card</title>
<link href="https://fonts.googleapis.com/css2?family=Didact+Gothic&display=swap" rel="stylesheet">
<style>
  :root {
    --backdrop: #f5ecdd;
    --gold-dark: #c08a22;
    --gold-light: #f4e1a6;
    --gold-deep: #b8780c;
    --navy-deep: #0a1850;
    --navy-mid: #1c3a8e;
    --navy-light: #3059c0;
    --brand-blue: #1f2fd6;
    --brand-ink: #16206e;
    --text-light: #ffffff;
  }
  * { margin: 0; padding: 0; box-sizing: border-box; }
  html, body {
    width: 1200px;
    height: 721px;
    overflow: hidden;
    background: var(--backdrop);
  }
  .business-card {
    position: absolute;
    left: 241px;
    top: 155px;
    width: 718px;
    height: 410px;
    overflow: hidden;
    box-shadow: 0 2px 6px rgba(0, 0, 0, 0.12);
    font-family: "Didact Gothic", sans-serif;
  }
  .card-art {
    position: absolute;
    inset: 0;
    width: 100%;
    height: 100%;
  }
  .brand {
    position: absolute;
    left: 34px;
    top: 56px;
    display: flex;
    align-items: center;
    gap: 16px;
  }
  .brand-dot {
    width: 64px;
    height: 64px;
    border-radius: 50%;
    background: var(--brand-blue);
  }
  .brand-name {
    font-size: 38px;
    letter-spacing: 1px;
    color: var(--brand-ink);
    line-height: 1;
  }
  .contact {
    position: absolute;
    right: 55px;
    top: 170px;
    text-align: right;
    color: var(--text-light);
  }
  .contact-name {
    font-size: 38px;
    line-height: 46px;
  }
  .contact-line {
    font-size: 26px;
    line-height: 41px;
  }
</style>
</head>
<body>
  <div class="business-card">
    <svg class="card-art" viewBox="0 0 718 410" xmlns="http://www.w3.org/2000/svg">
      <defs>
        <linearGradient id="gold-band" x1="0" y1="0" x2="1" y2="0">
          <stop offset="0" stop-color="var(--gold-dark)"/>
          <stop offset="0.35" stop-color="var(--gold-light)"/>
          <stop offset="0.6" stop-color="#e8c977"/>
          <stop offset="1" stop-color="var(--gold-deep)"/>
        </linearGradient>
        <linearGradient id="navy-field" x1="0" y1="0" x2="1" y2="1">
          <stop offset="0" stop-color="var(--navy-mid)"/>
          <stop offset="0.5" stop-color="var(--navy-light)"/>
          <stop offset="1" stop-color="var(--navy-deep)"/>
        </linearGradient>
      </defs>
      <rect width="718" height="410" fill="url(#gold-band)"/>
      <path role="img" aria-label="Navy hexagonal cube pattern background"
            d="M0,212 C200,228 380,190 520,158 S680,112 718,108 L718,410 L0,410 Z"
            fill="url(#navy-field)"/>
      <path d="M0,212 C200,228 380,190 520,158 S680,112 718,108"
            fill="none" stroke="#ffffff" stroke-width="4"/>
    </svg>

    <div class="brand">
      <span class="brand-dot"></span>
      <span class="brand-name">QUORVEX HUB</span>
    </div>

    <div class="contact">
      <p class="contact-name">Ravi Tanner</p>
      <p class="contact-line">Senior Security Engineer</p>
      <p class="contact-line">ravi.tanner@quorvex-hub.com</p>
      <p class="contact-line">877.640.3958</p>
      <p class="contact-line">www.quorvex-hub.com</p>
    </div>
  </div>
</body>
</html>
```